Stonebrook Dugout case study mailout

Project must be designed in Adobe Illustrator.
I need a 8.5" x 11" brochure that will be folded in half and sent out as a mailout. I have attached our previous mailout and want some overlap in format to maintain our "brand". For the top part, I want the logo to stay on the left and blank space on the right (which is where my address label and stamp go).
I have attached the content in a word document (Stonebrook ).
I have attached a rough image of what I think the front could be, as far as the image. I would like the quote on the front as well, and the results.
I've included some photos of the dugout that are in the word document, whether or not they would show well on the brochure I don't know. These are the "after" photos and unfortunately I don't currently have the "before" ones.
Our website is www.ridgelandpumpworks.example and the system we sell is from www.vantorel-aqua.example (also our company - manufacturing division).

```html
<!DOCTYPE html>
<html lang="en">
<head>
<meta charset="utf-8">
<title>Stonebrook Dugout Case Study Mailout</title>
<link href="https://fonts.googleapis.com/css2?family=Open+Sans:ital,wght@0,400;0,600;0,700;0,800;1,700&display=swap" rel="stylesheet">
<style>
:root{
  --blue:#2f6fc1;
  --blue-dark:#1f4f96;
  --gold:#d9c27a;
  --gold-dark:#b89b45;
  --ink:#2b2b2b;
  --footer:#1e1e1e;
  --paper:#ffffff;
  --stage:#dcdcdf;
  --water:#6f8c86;
  --sand:#c9b89a;
}
*{box-sizing:border-box;margin:0;padding:0}
html,body{width:900px;height:1200px;overflow:hidden}
body{background:var(--stage);font-family:"Open Sans",sans-serif;color:var(--ink);position:relative}
.spread{position:absolute;left:0;top:309px;width:900px;height:582px;display:flex;box-shadow:0 6px 18px rgba(0,0,0,.18)}
.page{position:relative;width:450px;height:582px;background:var(--paper);overflow:hidden}
.page--inside{border-right:1px solid #e4e4e4}

/* inside page */
.photo{position:absolute;border-radius:10px;border:3px solid #ececec;background:linear-gradient(160deg,#9aa3a8,#6f7a80 55%,#c7ccc9)}
.photo--plant-a{left:16px;top:14px;width:200px;height:138px}
.photo--plant-b{left:232px;top:14px;width:200px;height:138px;background:linear-gradient(160deg,#b9bfc0,#7d8a8c 55%,#d2d6d3)}
.details{position:absolute;left:16px;top:162px;width:150px}
.h-blue{color:var(--blue);font-weight:800;font-size:10px;text-transform:uppercase}
.h-gold{color:var(--gold-dark);font-weight:700;font-size:8px}
.details ul{list-style:none;margin-top:4px}
.details li{font-size:7px;line-height:1.3;margin-bottom:4px;padding-left:9px;position:relative}
.details li::before{content:"";position:absolute;left:0;top:3px;width:4px;height:4px;border-radius:50%;background:var(--blue)}
.objective{position:absolute;left:168px;top:162px;width:268px;font-size:7px;line-height:1.35}
.objective strong{font-size:8.5px;display:block;margin-bottom:5px}
.pill{display:inline-block;background:var(--blue);color:#fff;font-weight:700;font-size:7px;border-radius:10px;padding:2px 10px;margin:4px 0}
.band-blue{position:absolute;left:0;top:262px;width:450px;height:34px;background:var(--blue);color:#fff}
.band-blue .label{position:absolute;left:34px;top:6px;font-weight:800;font-size:9px;line-height:1.1;text-align:center}
.stat{position:absolute;top:4px;text-align:center;font-size:6.5px;line-height:1.15}
.stat span{display:block;background:var(--gold);color:var(--ink);font-weight:700;font-size:6px;border-radius:6px;padding:1px 6px;margin-bottom:1px}
.band-gold{position:absolute;left:0;top:296px;width:450px;height:18px;background:var(--gold);color:#fff;font-weight:800;font-size:10px;text-align:center;line-height:18px}
.col{position:absolute;top:322px;width:200px}
.col--l{left:18px}.col--r{left:232px}
.item{margin-bottom:7px}
.item p{font-size:6.5px;line-height:1.3}
.item .h-gold{text-transform:uppercase;display:flex;align-items:center;gap:4px;margin-bottom:1px}
.item .h-blue{font-size:10.5px;margin-bottom:2px}
.dot{width:7px;height:7px;border-radius:50%;background:var(--blue);display:inline-block}

/* cover page */
.brand{position:absolute;left:26px;top:58px;font-weight:800;font-size:30px;color:var(--blue);letter-spacing:-.5px}
.mark{display:inline-block;width:14px;height:14px;background:var(--blue);margin-right:7px;vertical-align:4px}
.cover-band{position:absolute;left:0;top:168px;width:450px;height:24px;background:var(--gold);color:#fff;font-weight:800;font-size:11.5px;line-height:24px;padding-left:26px;text-transform:uppercase}
.hero{position:absolute;left:0;top:192px;width:450px;height:372px;background:linear-gradient(170deg,#9fb0ae 0%,var(--water) 40%,#4f5d5c 62%,var(--sand) 78%,#b9aa8c 100%)}
.intro{position:absolute;left:20px;top:350px;width:265px;background:#fff;padding:10px 12px;font-size:7.3px;line-height:1.42;text-align:justify}
.colony{position:absolute;left:292px;top:282px;width:158px;background:var(--blue);color:#fff;padding:10px 12px;clip-path:polygon(14px 0,100% 0,100% 100%,0 100%,0 14px)}
.colony h3{font-size:10px;font-weight:800;margin-bottom:7px}
.colony dt{color:var(--gold);font-weight:800;font-size:9px;text-transform:uppercase}
.colony dd{font-weight:700;font-size:7.5px;margin-bottom:5px;line-height:1.2}
.footer{position:absolute;left:12px;top:480px;width:438px;height:62px;background:var(--footer);color:#fff;border-radius:16px 0 0 16px;padding:8px 16px;font-size:9px}
.footer .call{font-weight:800;font-style:italic;font-size:12px}
.footer .row{display:flex;align-items:center;gap:5px;margin-top:3px}
.footer svg{flex:none}
</style>
</head>
<body>
<div class="spread">

  <section class="page page--inside">
    <div class="photo photo--plant-a" role="img" aria-label="Photo of the treatment building with ozone equipment and tanks"></div>
    <div class="photo photo--plant-b" role="img" aria-label="Photo of the treatment room with ozone generator units"></div>

    <div class="details">
      <h2 class="h-blue">Project Details</h2>
      <div class="h-gold" style="font-size:8px;margin-top:2px">Equipment:</div>
      <ul>
        <li>Vantorel Aqua V-160 Ozone Generator</li>
        <li>OxyLine OC-2 Oxygen Concentrator</li>
        <li>Nanobubble Injection</li>
      </ul>
    </div>

    <div class="objective">
      <strong>Objective: Treat and maintain dugout water quality</strong>
      Treatment Configuration: Recirculating into the dugout with single inlet and outlet. Intake from 45 feet deep in middle of reservoir, and return about 30 feet from water's edge.<br>
      <span class="pill">Diffusion Method: Nanobubbles</span><br>
      Previous Treatment: &bull; Conventional Aeration &nbsp;&nbsp;&bull; Chemicals (if applicable)
    </div>

    <div class="band-blue">
      <div class="label">WATER<br>CONSUMPTION</div>
      <div class="stat" style="left:150px"><span>DAILY USE</span>Approximately<br>70,000 Gallons</div>
      <div class="stat" style="left:250px"><span>DUGOUT VOLUME</span>30,000,000 Gallons</div>
      <div class="stat" style="left:350px"><span>FLOW RATE</span>Continuous at 50 GPM</div>
    </div>
    <div class="band-gold">RESULTS AND OBSERVATIONS – THE DUGOUT</div>

    <div class="col col--l">
      <div class="item"><div class="h-gold"><i class="dot"></i>ORP Improvement</div><p>Within two weeks, the Oxidation-Reduction Potential (ORP) increased by approximately 350mV, from -100mV to 250mV.</p></div>
      <div class="item"><div class="h-gold"><i class="dot"></i>Algae Reduction</div><p>Previously, there was a 1-inch thick layer of algae on the edge of the pond; now, only a thin layer of sand remains.</p></div>
      <div class="item"><div class="h-blue">Cistern Observations</div><p>Water clarity has significantly improved, allowing visibility to the bottom of the cistern, which was previously obscured by algae and other contaminants.</p></div>
      <div class="item"><div class="h-blue">Additional Benefits</div><p>&bull; The brown ring that used to form in residential drains and tubs is no longer occurring.</p></div>
    </div>
    <div class="col col--r">
      <div class="item"><div class="h-gold"><i class="dot"></i>Foam Reduction</div><p>Within two weeks, the Oxidation-Reduction Potential (ORP) increased by approximately 350mV, from -100mV to 250mV.</p></div>
      <div class="item"><div class="h-gold"><i class="dot"></i>Water Clarity</div><p>Previously, there was a 1-inch thick layer of algae on the edge of the pond; now, only a thin layer of sand remains.</p></div>
      <div class="item"><div class="h-blue">Filtration Performance</div><p>&bull; Filter performance has greatly improved since introducing ozone to the dugouts.</p><p>&bull; Small particulate and dissolved organic matter are being effectively flocculated, allowing filters to capture more material.</p><p>&bull; Small particulate and dissolved organic matter are being effectively flocculated, allowing filters to capture more material.</p></div>
    </div>
  </section>

  <section class="page page--cover">
    <div class="brand"><i class="mark"></i>Ridgeland Pumpworks</div>
    <div class="cover-band">Case Study: Dugout Treatment at Stonebrook Colony</div>
    <div class="hero" role="img" aria-label="Photo of the lined dugout with the nanobubble intake pipe on the sandy bank"></div>

    <p class="intro">This case study highlights the effectiveness of the Vantorel Aqua V160 unit and nanobubble injectors in improving water quality at Stonebrook Colony near Marwick, Alberta. Within only two weeks of treating the dugout water, a drastic improvement in water quality was observed in the reservoir and in downstream applications. Water is at the heart of life on Stonebrook Colony for its people, livestock and crops. Vantorel Aqua is providing this hard-working community with the equipment needed to be healthy and thrive with a pure, clean, reliable water supply.</p>

    <div class="colony">
      <h3>COLONY INFORMATION</h3>
      <dl>
        <dt>Name:</dt><dd>Stonebrook Hutterite Colony</dd>
        <dt>Water Usage</dt><dd>Dairy, Chickens, Swine, Field Crops, Drinking Water</dd>
        <dt>Location</dt><dd>Central Alberta</dd>
      </dl>
    </div>

    <div class="footer">
      <div class="row"><span class="call">Call us Anytime</span>
        <svg width="9" height="11" viewBox="0 0 9 11" style="margin-left:14px"><rect x="1" y="0.5" width="7" height="10" rx="1.5" fill="none" stroke="#d9c27a" stroke-width="1.2"/></svg>
        <span>Toll Free: 1-800-555-0147 or Local: 1-780-555-0162</span></div>
      <div class="row">
        <svg width="10" height="10" viewBox="0 0 10 10"><circle cx="5" cy="5" r="4.2" fill="none" stroke="#d9c27a" stroke-width="1.2"/></svg>
        <span>www.ridgelandpumpworks.example</span>
        <svg width="11" height="8" viewBox="0 0 11 8" style="margin-left:14px"><rect x=".5" y=".5" width="10" height="7" fill="#d9c27a"/><path d="M.5 .5 5.5 4.5 10.5 .5" fill="none" stroke="#1e1e1e"/></svg>
        <span>info@ridgelandpumpworks.example</span>
      </div>
    </div>
  </section>

</div>
</body>
</html>
```